Family Business Father/Son Consulting team needs a cover for their book on family workplace dynamics

We are a father/son consulting firm that focuses on the psychology of communication and performance in the workplace of financial advisors. We recently wrote a book on the topic of family members working in the same financial services practice together. So, we need someone to design the cover for our book. The book itself is in a self-help style with the occasional exercise. It is psychologically based and while specific to the finance industry, does not discuss finances itself.

We would like the cover to clearly communicate that this book is practical, easy to read, and impactful. The average reader is someone who is successful in business and work or will soon plan on working with a family member.

The Title is "The Steady Kinship Crew: Shaping, Growing, and Handing Over a Household Enterprise in Wealth Advising" by Owen Pelkart, KTC*TM(this should be a trademark) and Rob Pelkart, Ph.D. Foreword by Joan Merrow.

Target Market(s)

Financial advisors who work with family members. Usually it is a parent/child, but not always.

Industry/Entity Type

Consulting within Financial Services

Colors

Designer to choose colors to be used in the design.

Requirements
Must have
• The ability for the design to be a printed book and for E-book
Nice to have
• Could be a simple design with the title or with graphics,. We are open to either. Our business colors are in the royal blue range. So, that color scheme could be nice, but isn't essential if there is something more creative/better that you have in mind.
Should not have
• Extravagant/ too playful of colors, but can be fun with design

```html
<!DOCTYPE html>
<html lang="en">
<head>
<meta charset="utf-8">
<title>The Steady Kinship Crew — Book Cover</title>
<link rel="stylesheet" href="https://fonts.googleapis.com/css2?family=Josefin+Sans:wght@400;600;700&display=swap">
<style>
  :root {
    --backdrop: #2f2824;
    --cover-blue-light: #3a5796;
    --cover-blue-mid: #24407e;
    --cover-blue-deep: #182b5c;
    --ink-white: #ffffff;
    --ink-soft: #e8ecf6;
  }
  * { margin: 0; padding: 0; box-sizing: border-box; }
  html, body {
    width: 1200px;
    height: 1200px;
    overflow: hidden;
    background: var(--backdrop);
  }
  .canvas {
    position: relative;
    width: 1200px;
    height: 1200px;
  }
  .book-cover {
    position: absolute;
    left: 258px;
    top: 78px;
    width: 686px;
    height: 1028px;
    overflow: hidden;
    font-family: "Josefin Sans", sans-serif;
    color: var(--ink-white);
  }
  .cover-photo {
    position: absolute;
    inset: 0;
    background:
      radial-gradient(ellipse at 50% 45%, var(--cover-blue-light) 0%, var(--cover-blue-mid) 55%, var(--cover-blue-deep) 100%);
  }
  .title-block {
    position: absolute;
    left: 89px;
    top: 174px;
    right: 30px;
  }
  .book-title {
    font-weight: 600;
    font-size: 56px;
    line-height: 1.12;
    letter-spacing: 2px;
    text-transform: uppercase;
  }
  .book-subtitle {
    margin-top: 14px;
    font-weight: 400;
    font-size: 16.5px;
    line-height: 1.45;
    letter-spacing: 2.4px;
    text-transform: uppercase;
    color: var(--ink-soft);
  }
  .credits {
    position: absolute;
    left: 89px;
    top: 848px;
  }
  .author {
    font-weight: 600;
    font-size: 23px;
    letter-spacing: 2.4px;
    text-transform: uppercase;
    line-height: 1;
  }
  .author + .author { margin-top: 26px; }
  .foreword {
    margin-top: 20px;
    font-weight: 600;
    font-size: 16px;
    letter-spacing: 1.6px;
  }
</style>
</head>
<body>
  <main class="canvas">
    <section class="book-cover">
      <div class="cover-photo" role="img" aria-label="Blue-toned photograph of a family climbing a wide flight of outdoor stairs together"></div>

      <header class="title-block">
        <h1 class="book-title">The Steady<br>Kinship Crew</h1>
        <p class="book-subtitle">Shaping, Growing, and Handing Over<br>A Household Enterprise in Wealth Advising</p>
      </header>

      <footer class="credits">
        <p class="author">Owen Pelkart, KTC™</p>
        <p class="author">and Rob Pelkart, Ph.D.</p>
        <p class="foreword">Foreword by Joan Merrow</p>
      </footer>
    </section>
  </main>
</body>
</html>
```